RWT Installations Ltd Business Cards

We need a business card with our business logo. We provide window and door installations on high-rises in west coast British Colombia, Canada.

I would like my business information and details on one side of the card, and the other side the company name with logo

Target Market(s)

General Contractors

Industry/Entity Type

Construction

Contact Information for Business Card

one side i want my company name and logo in the dark theme logo that i provided

Requirements
Must have
• Tomas Verelund, 15559284016, RWTInstallations@mailvera.example, 1408-5192 Pellow Avenue Burnaby BC, V0X 1Z9, Owner & Manager

```html
<!DOCTYPE html>
<html lang="en">
<head>
<meta charset="utf-8">
<title>RWT Installations Ltd – Business Card</title>
<link href="https://fonts.googleapis.com/css2?family=Lato:wght@400;700&display=swap" rel="stylesheet">
<style>
  :root {
    --backdrop: #2a2a2a;
    --card-dark: #1f1f1f;
    --card-light: #ffffff;
    --brand-blue: #27a3df;
    --brand-grey: #9a9a9a;
    --text-dark: #4a4a4a;
  }
  * { box-sizing: border-box; margin: 0; padding: 0; }
  html, body { width: 1200px; height: 900px; overflow: hidden; }
  body {
    background: var(--backdrop);
    font-family: "Lato", sans-serif;
    display: flex;
    flex-direction: column;
    align-items: center;
    justify-content: center;
    gap: 36px;
  }
  .card {
    width: 700px;
    height: 400px;
    border-radius: 26px;
    position: relative;
    overflow: hidden;
    box-shadow: 0 10px 30px rgba(0,0,0,0.45);
  }
  .card-front {
    background: var(--card-dark);
    display: flex;
    align-items: center;
    justify-content: center;
  }
  .brand-lockup {
    display: flex;
    align-items: center;
    gap: 22px;
  }
  .brand-square {
    width: 64px;
    height: 64px;
    background: var(--brand-blue);
  }
  .brand-name {
    color: var(--brand-blue);
    font-weight: 700;
    font-size: 44px;
    letter-spacing: 1px;
    line-height: 1.1;
  }
  .card-back { background: var(--card-light); }
  .identity {
    position: absolute;
    left: 30px;
    width: 300px;
    top: 150px;
    text-align: right;
  }
  .person-name {
    color: var(--brand-blue);
    font-weight: 700;
    font-size: 29px;
    letter-spacing: 0.3px;
    text-transform: uppercase;
    white-space: nowrap;
  }
  .person-title {
    color: var(--brand-grey);
    font-size: 19px;
    margin-top: 4px;
  }
  .divider {
    position: absolute;
    left: 352px;
    top: 110px;
    width: 1.5px;
    height: 160px;
    background: var(--brand-blue);
  }
  .contact-list {
    position: absolute;
    left: 376px;
    top: 104px;
    list-style: none;
    color: var(--text-dark);
    font-size: 15px;
    line-height: 1.35;
  }
  .contact-list li {
    display: flex;
    align-items: flex-start;
    gap: 10px;
    margin-bottom: 5px;
    white-space: nowrap;
  }
  .contact-list svg {
    width: 14px;
    height: 14px;
    flex: none;
    margin-top: 2px;
    fill: var(--brand-blue);
  }
  .corner-brand {
    position: absolute;
    right: 34px;
    bottom: 30px;
    display: flex;
    align-items: center;
    gap: 8px;
  }
  .corner-brand .brand-square { width: 22px; height: 22px; }
  .corner-brand .brand-name { font-size: 15px; letter-spacing: 0.3px; }
</style>
</head>
<body>
  <section class="card card-front">
    <div class="brand-lockup">
      <span class="brand-square"></span>
      <span class="brand-name">RWT Installations Ltd</span>
    </div>
  </section>

  <section class="card card-back">
    <div class="identity">
      <div class="person-name">Tomas Verelund</div>
      <div class="person-title">Owner &amp; Manager</div>
    </div>
    <div class="divider"></div>
    <ul class="contact-list">
      <li>
        <svg viewBox="0 0 24 24"><path d="M12 2a7 7 0 0 0-7 7c0 5 7 13 7 13s7-8 7-13a7 7 0 0 0-7-7zm0 9.5A2.5 2.5 0 1 1 12 6a2.5 2.5 0 0 1 0 5.5z"/></svg>
        <span>1408-5192 Pellow Avenue<br>Burnaby BC, V0X 1Z9</span>
      </li>
      <li>
        <svg viewBox="0 0 24 24"><path d="M6.6 10.8a15.1 15.1 0 0 0 6.6 6.6l2.2-2.2c.3-.3.7-.4 1-.2 1.1.4 2.3.6 3.6.6.6 0 1 .4 1 1V20c0 .6-.4 1-1 1A17 17 0 0 1 3 4c0-.6.4-1 1-1h3.5c.6 0 1 .4 1 1 0 1.3.2 2.5.6 3.6.1.3 0 .7-.2 1z"/></svg>
        <span>(555) 928-4016</span>
      </li>
      <li>
        <svg viewBox="0 0 24 24"><path d="M7 1h10a2 2 0 0 1 2 2v18a2 2 0 0 1-2 2H7a2 2 0 0 1-2-2V3a2 2 0 0 1 2-2zm0 3v14h10V4zm5 15.5a1 1 0 1 0 0 2 1 1 0 0 0 0-2z"/></svg>
        <span>(555) 928-4016</span>
      </li>
      <li>
        <svg viewBox="0 0 24 24"><path d="M6 2h12v5H6zM4 8h16a2 2 0 0 1 2 2v7h-4v5H6v-5H2v-7a2 2 0 0 1 2-2zm4 8v4h8v-4z"/></svg>
        <span>(555) 928-4016</span>
      </li>
      <li>
        <svg viewBox="0 0 24 24"><path d="M2 5h20v14H2zm2 2v.5l8 5 8-5V7zm0 2.8V17h16V9.8l-8 5z"/></svg>
        <span>RWTInstallations@mailvera.example</span>
      </li>
      <li>
        <svg viewBox="0 0 24 24"><path d="M12 2a10 10 0 1 0 0 20 10 10 0 0 0 0-20zm-1 17.9A8 8 0 0 1 4.1 11H7c.1 3 1.5 6 4 8.9zM4.1 9A8 8 0 0 1 11 4.1C8.5 7 7.2 8 7 9zm8.9 10.9c2.5-2.9 3.9-5.9 4-8.9h2.9a8 8 0 0 1-6.9 8.9zM17 9c-.2-1-1.5-2-4-4.9A8 8 0 0 1 19.9 9z"/></svg>
        <span>rwtinstallations.example</span>
      </li>
    </ul>
    <div class="corner-brand">
      <span class="brand-square"></span>
      <span class="brand-name">RWT Installations Ltd</span>
    </div>
  </section>
</body>
</html>
```